Inner pages of website needed (2 pages)

Hi there,

I am in the process of designing a new website (Foundation/HTML - no CMS being used). It's to replace an existing site. The home page is fine, but I need the inner pages improved. I do have some inner pages already produced, but I'm not happy with them.

The new website home page can be found here http://webfolkly.com/project-demo/zephyr/index.html
(this is the style concept).

The old website can be found here:
http://cv-harbourline.com.au/

To start, I will need 2 pages designed based on the new style, but migrating the information from the old site:

Resume Services Page (http://cv-harbourline.com.au/professional-resumes.html). On the original page you'll see a number of headings:

Career Resources Page (http://cv-harbourline.com.au/career-advice.html)

If possible, I'd like to integrate any new ideas you may have from a design perspective.

Let me know what else you need from me.

Target Market(s)

Professionals

Industry/Entity Type

Professional Service

Number of Pages Required

2 page

Colors
3176b5
0355a3
85abd2
add136
cadf82
f68d4d
f37122
f78f20

Requirements
Must have
• Please pay particular attention to the design of the new home page and consider this as a style guide. Needs to have similar fonts, look professional and clean.
Nice to have
• Some additional functionality perhaps pictures/text interchanging.

```html
<!DOCTYPE html>
<html lang="en">
<head>
<meta charset="utf-8">
<title>Career Resources – Harbourline Professional Solutions</title>
<link href="https://fonts.googleapis.com/css2?family=Lato:wght@400;700&family=Roboto:wght@300;400&display=swap" rel="stylesheet">
<style>
:root{
  --blue:#3176b5;
  --blue-deep:#0355a3;
  --blue-light:#85abd2;
  --green:#add136;
  --green-pale:#cadf82;
  --orange:#f37122;
  --orange-soft:#f68d4d;
  --gold:#c9a437;
  --text:#3a3a3a;
  --muted:#666;
  --panel-left:#f4f4f4;
  --panel-right:#ebebeb;
}
*{box-sizing:border-box;margin:0;padding:0}
html,body{width:740px;height:1200px;overflow:hidden}
body{position:relative;font-family:'Lato',sans-serif;color:var(--text);background:#fff}
.abs{position:absolute}
a{color:var(--blue);text-decoration:none}

/* header */
.site-header{position:absolute;left:0;top:0;width:740px;height:68px;background:var(--blue)}
.brand{left:97px;top:20px;color:#fff;font-size:24px;font-weight:700;letter-spacing:.5px}
.brand-sub{left:97px;top:48px;color:#fff;font-size:7.5px;letter-spacing:.6px}
.main-nav{left:278px;top:29px;display:flex;gap:13px;font-size:8.6px;color:#fff}
.main-nav span{padding-bottom:4px}
.main-nav .active{border-bottom:1.5px solid #fff}

/* hero */
.hero{left:0;top:68px;width:740px;height:204px;background:linear-gradient(90deg,#2b6aa6,#3a82c2 50%,#2b6aa6)}
.hero-person-left{left:140px;top:78px;width:120px;height:170px;background:linear-gradient(180deg,#c79a80,#d9a6b2 45%,#6f7a5a);border-radius:50px 50px 6px 6px;opacity:.85}
.hero-person-right{left:430px;top:74px;width:180px;height:198px;background:linear-gradient(180deg,#d8b39b,#f3f5f7 55%,#e8edf2);border-radius:70px 70px 0 0;opacity:.9}
.hero-title{left:0;width:740px;top:118px;text-align:center;color:#fff;font-size:26px;font-weight:700;padding-left:14px}
.hero-tag{left:332px;top:148px;color:#fff;font-size:9px}
.crumb-bar{left:0;top:246px;width:740px;height:26px;background:rgba(20,60,100,.45)}
.crumb{left:98px;top:254px;color:#fff;font-size:8px;display:flex;align-items:center;gap:6px}
.crumb b{font-weight:700}

/* intro */
.intro-head{left:0;width:740px;top:293px;text-align:center;color:var(--blue);font-size:14px;font-weight:700}
.rule{height:1px;background:#e2e2e2}
.intro-text{left:98px;width:544px;top:343px;text-align:center;font-size:9.4px;line-height:17px;color:var(--text)}
.btn-orange{left:269px;top:391px;width:201px;height:24px;border:1px solid var(--orange);border-radius:2px;color:var(--orange);font-size:9px;display:flex;align-items:center;justify-content:center}

/* looks band */
.looks{left:0;top:438px;width:740px;height:192px;background:var(--blue)}
.looks-head{left:0;width:740px;top:459px;text-align:center;color:#fff;font-size:14px;font-weight:700}
.looks-rule{left:98px;top:493px;width:544px;border-top:1px dotted rgba(255,255,255,.6)}
.looks-text{left:98px;top:514px;width:370px;color:#fff;font-family:Arial,sans-serif;font-size:9.4px;line-height:14px}
.btn-outline{left:98px;top:572px;width:230px;height:24px;border:1px solid #fff;border-radius:2px;color:#fff;font-size:9px;display:flex;align-items:center;justify-content:center}
.portrait-frame{left:495px;top:506px;width:146px;height:100px;background:#5b93c9;padding:4px}
.portrait{width:100%;height:100%;background:linear-gradient(135deg,#e8eef3,#c9d8e6 60%,#a9c1d8)}

/* resource columns */
.col-left{left:0;top:630px;width:301px;height:332px;background:var(--panel-left)}
.col-right{left:301px;top:630px;width:439px;height:332px;background:var(--panel-right)}
.col-head{color:var(--blue);font-size:14.5px;font-weight:700}
.col-rule{height:1px;background:#dcdcdc}
.res-text{font-family:Arial,sans-serif;font-size:9.2px;line-height:14px;color:var(--text)}
.res-link{font-family:Arial,sans-serif;font-size:9.2px;color:var(--blue)}

/* footer */
.foot-band{left:0;top:962px;width:740px;height:208px;background:var(--blue-light)}
.foot-card{left:90px;top:974px;width:560px;height:184px;background:#fff}
.foot-photo{left:98px;top:978px;width:201px;height:180px;background:linear-gradient(135deg,#f1f1f1,#d9d9d9 55%,#9ec9b5)}
.foot-h{font-family:'Roboto',sans-serif;font-weight:300;font-size:15px;color:#222}
.foot-small{font-size:7.2px;color:#555}
.foot-label{font-size:7.2px;font-weight:700;color:#222}
.news-input{left:310px;top:1133px;width:101px;height:17px;background:#8a8a8a;color:#d8d8d8;font-size:6.5px;padding:5px 4px}
.news-btn{left:411px;top:1133px;width:43px;height:17px;background:var(--green-pale);color:#333;font-size:7px;display:flex;align-items:center;justify-content:center}
.badge-laurel{left:472px;top:1014px;width:74px;height:40px;border:2px solid var(--gold);border-radius:20px}
.badge-banner{left:546px;top:1015px;width:96px;height:33px;background:var(--orange)}
.medal{top:1070px;width:22px;height:22px;border-radius:50%;background:var(--gold)}
.badge-member{left:572px;top:1072px;width:70px;height:20px;background:#dde3ec}
.seal{top:1110px;width:38px;height:38px;border-radius:50%;background:var(--orange-soft);border:2px solid var(--orange)}

.bottom-bar{left:0;top:1170px;width:740px;height:30px;background:var(--blue)}
.copyright{left:98px;top:1181px;color:#fff;font-size:7.4px}
.social{top:1175px;width:20px;height:20px;border-radius:50%;background:#fff}
</style>
</head>
<body>

<header class="site-header"></header>
<div class="abs brand">Harbourline</div>
<div class="abs brand-sub">PROFESSIONAL SOLUTIONS</div>
<nav class="abs main-nav">
  <span>HOME</span><span>ABOUT</span><span>RESUME SERVICES</span><span class="active">CAREER RESOURCES</span><span>PORTFOLIO</span><span>CONTACT US</span>
</nav>

<section class="abs hero" role="img" aria-label="Mosaic of professional portrait photos in blue tint"></section>
<div class="abs hero-person-left" role="img" aria-label="Photo of a smiling student holding books"></div>
<div class="abs hero-person-right" role="img" aria-label="Photo of a businessman in shirt and tie"></div>
<h1 class="abs hero-title">Career resources</h1>
<div class="abs hero-tag">Your challenge is our progress</div>
<div class="abs crumb-bar"></div>
<div class="abs crumb">
  <svg width="11" height="10" viewBox="0 0 11 10"><path d="M5.5 0L0 5h1.5v5h3V7h2v3h3V5H11z" fill="#fff"/></svg>
  <span>/</span><b>Career resources</b>
</div>

<h2 class="abs intro-head">CAREER &nbsp;ADVICE &amp; EMPLOYMENT TRENDS FOR 2016</h2>
<div class="abs rule" style="left:98px;top:326px;width:544px"></div>
<p class="abs intro-text">As we move into an Employers Driven Market, planning the right strategy can be critical to seeking success. The Hidden Job Market can be an extremely useful ally in understanding what's beneath the surface.</p>
<a class="abs btn-orange">The hidden job market - find out more here&nbsp;⟶</a>

<section class="abs looks"></section>
<h2 class="abs looks-head">How far will looks GET YOU?</h2>
<div class="abs looks-rule"></div>
<p class="abs looks-text">Are you Australia's next top model or just your average Joe? How far do employers judge a book by its cover? Here we look at a few simple measures that can make a world of difference.</p>
<a class="abs btn-outline">Simple dress sense can make a world of difference &nbsp;»</a>
<div class="abs portrait-frame"><div class="portrait" role="img" aria-label="Photo of a smiling young man in a blue shirt"></div></div>

<section class="abs col-left"></section>
<section class="abs col-right"></section>

<h3 class="abs col-head" style="left:98px;top:650px">Career essentials</h3>
<div class="abs col-rule" style="left:98px;top:678px;width:180px"></div>
<p class="abs res-text" style="left:98px;top:688px;width:180px">Before you even begin your employment search, there are a few basic rules to follow:-</p>
<a class="abs res-link" style="left:98px;top:740px">› Preparation is critical...[+]</a>
<div class="abs col-rule" style="left:98px;top:762px;width:180px"></div>
<p class="abs res-text" style="left:98px;top:772px;width:180px">Recruitment agencies - are they friends or foe? Whether you like them or not, you'll need to learn some basic principles to avoid being "blacklisted" !!!</p>
<a class="abs res-link" style="left:98px;top:838px">› &nbsp;Working with recruitment agencies...[+]</a>
<div class="abs col-rule" style="left:98px;top:861px;width:180px"></div>
<p class="abs res-text" style="left:98px;top:871px;width:180px">Not sure what money you should be asking for? Here's a rundown on just how to approach salary advice</p>
<a class="abs res-link" style="left:98px;top:923px">› &nbsp;Salary advice here...[+]</a>

<h3 class="abs col-head" style="left:324px;top:650px">FURTHER CAREER RESOURCES</h3>
<p class="abs res-text" style="left:324px;top:688px;width:320px">Just how important is it to understand the differences in the market today ?</p>
<a class="abs res-link" style="left:324px;top:712px">› &nbsp;A look into an employers driven market...[+]</a>
<p class="abs res-text" style="left:324px;top:742px;width:320px">At some point during your life, you will consider a change in career, but how simple is this to do? Here we provide some practical career advice services about how to approach this subject.</p>
<a class="abs res-link" style="left:324px;top:794px">› &nbsp;Changing careers, career advice here...[+]</a>
<p class="abs res-text" style="left:324px;top:826px;width:320px">Worried if your age will get in the way? Find out more about how to avoid the age trap</p>
<a class="abs res-link" style="left:324px;top:862px">› &nbsp;Age awareness career advice here...[+]</a>
<p class="abs res-text" style="left:324px;top:894px;width:320px">Free resume templates, resume blasters, 5 minute resumes. What's really happening there?</p>
<a class="abs res-link" style="left:324px;top:931px">› &nbsp;Resume templates and software...[+]</a>

<footer class="abs foot-band"></footer>
<div class="abs foot-card"></div>
<div class="abs foot-photo" role="img" aria-label="Photo of a consultant on the phone at a desk with a laptop"></div>

<h4 class="abs foot-h" style="left:310px;top:987px">Contact Us</h4>
<div class="abs foot-small" style="left:310px;top:1007px;color:var(--blue)">Send Me a Message / Contact Info</div>
<div class="abs foot-label" style="left:310px;top:1030px">Address</div>
<div class="abs foot-small" style="left:310px;top:1042px">full Address goes here, cityname, country</div>
<div class="abs foot-small" style="left:310px;top:1065px"><span class="foot-label">Phone :</span> (415) 555-0142</div>
<div class="abs foot-small" style="left:310px;top:1077px"><span class="foot-label">Email:</span> <span style="color:var(--blue)">hello@harbourline.example</span></div>
<div class="abs foot-small" style="left:310px;top:1100px"><span class="foot-label">Fax:</span> 1-212-555-0190</div>
<div class="abs foot-label" style="left:310px;top:1123px">Subscribe Newsletter</div>
<div class="abs news-input">Enter your email</div>
<div class="abs news-btn">Submit</div>

<h4 class="abs foot-h" style="left:471px;top:987px">Awards &amp; Membership</h4>
<div class="abs badge-laurel"></div>
<div class="abs badge-banner"></div>
<div class="abs medal" style="left:474px"></div>
<div class="abs medal" style="left:498px"></div>
<div class="abs medal" style="left:522px"></div>
<div class="abs medal" style="left:546px"></div>
<div class="abs badge-member"></div>
<div class="abs seal" style="left:474px"></div>
<div class="abs seal" style="left:516px"></div>
<div class="abs seal" style="left:558px"></div>
<div class="abs seal" style="left:602px"></div>

<div class="abs bottom-bar"></div>
<div class="abs copyright">Copyright 2015 Harbourline Professional Solutions. All Rights Reserved.</div>
<div class="abs social" style="left:560px"></div>
<div class="abs social" style="left:581px"></div>
<div class="abs social" style="left:602px"></div>
<div class="abs social" style="left:623px"></div>

</body>
</html>
```